Business Card Design of an established Waste Management, Plastic Recycling and Renewable Energy Comp

We are looking for business card design for plastic card with holograms (Very similar to credit card). I will provide our logo (Fenwicks). So the name on the business card will be our logo )Fenwicks) + Environmental next to it, so it will read Fenwicks Environmental. The font for Environmental does not to be the same as the font of the logo. The holograms will be used to display ISO14001 Certified (In normal credit card, normally on the holograms, they show zenra or corvo). I will post the design requirements from the card printing company very shortly to make sure they can use the design for the plastic card.

Target Market(s)

Companies, Government Organizations, Corporations.

Industry/Entity Type

Business

Contact Information for Business Card

Motto (Under the logo): Done Properly, Always
Name: Bertolus Kemprano; Position: Business Manager; Address: Kestrel Vale Landfill & Recycling Facility, Wexcombe Rd, Marrowbank, WA 6197; Ph: +61 8 5021 3748; Mob: +61 400 917 352; E: Bertie@fenwicksenvironmental-mail.example

Requirements
Must have
• Business Names: Fenwicks Logo + Environmental word after the logo.
• Motto (Under the logo): Done Properly, Always
• All the Business Card Details above.
• Hologram Logo on the lower right corner which says: ISO 14001 Certified.
• Please remember the design will be printed on plastic card Not paper. The plastic crad is the same as credit card. Hope this helps. Thank You

```html
<!DOCTYPE html>
<html lang="en">
<head>
<meta charset="utf-8">
<title>Fenwicks Environmental – Business Card</title>
<link rel="stylesheet" href="https://fonts.googleapis.com/css2?family=Open+Sans:wght@300;400;600;700&display=swap">
<style>
  :root {
    --backdrop: #f1f2f2;
    --card: #ffffff;
    --ink-grey: #4b4b4e;
    --ink-soft: #626266;
    --brand-navy: #1b5ea0;
    --brand-sky: #1e9be0;
    --badge-deep: #0b4f96;
    --badge-light: #2aa3e3;
    --ghost: #ececec;
    --ghost-soft: #f0f0f0;
  }
  * { box-sizing: border-box; margin: 0; padding: 0; }
  html, body {
    width: 1200px; height: 588px; overflow: hidden;
    background: var(--backdrop);
    font-family: "Open Sans", Arial, sans-serif;
  }
  .canvas { position: relative; width: 1200px; height: 588px; }

  .card {
    position: absolute; top: 154px;
    width: 447px; height: 280px;
    background: var(--card);
    border-radius: 24px;
    overflow: hidden;
  }
  .card--front { left: 127px; }
  .card--back  { left: 626px; }

  /* Brand lockup */
  .lockup { position: absolute; inset: 0; }
  .lockup__dot {
    position: absolute; left: 35px; top: 108px;
    width: 62px; height: 62px; border-radius: 50%;
    background: var(--brand-sky);
  }
  .lockup__name {
    position: absolute; left: 104px; top: 106px;
    font-size: 44px; font-weight: 600; line-height: 1;
    color: var(--ink-grey); letter-spacing: -0.5px;
  }
  .lockup__motto {
    position: absolute; right: 34px; top: 150px;
    font-size: 16px; font-weight: 400; line-height: 20px; color: var(--brand-navy);
  }

  /* Faint show-through on back */
  .lockup--ghost { transform: scaleX(-1); }
  .lockup--ghost .lockup__dot { background: var(--ghost); }
  .lockup--ghost .lockup__name { color: var(--ghost); }
  .lockup--ghost .lockup__motto { color: var(--ghost-soft); }

  /* Address */
  .address {
    position: absolute; left: 38px; top: 214px;
    display: flex; align-items: center; gap: 8px;
  }
  .address__icon { width: 9px; height: 12px; flex: none; }
  .address__text {
    font-size: 12.5px; font-weight: 400; line-height: 18px; color: var(--ink-soft);
  }

  .cert-badge {
    position: absolute; left: 350px; top: 193px;
    width: 62px; height: 52px; border-radius: 6px;
    background: var(--badge-deep);
    display: flex; align-items: center; justify-content: center;
  }
  .cert-badge__disc {
    width: 37px; height: 37px; border-radius: 50%; background: var(--badge-light);
  }

  /* Back details */
  .person {
    position: absolute; left: 20px; top: 212px;
    line-height: 18px;
  }
  .person__name { font-size: 14px; font-weight: 400; color: var(--brand-navy); }
  .person__role { font-size: 14.5px; font-weight: 700; color: var(--brand-sky); }

  .divider {
    position: absolute; left: 167px; top: 212px;
    width: 1px; height: 39px; background: var(--brand-navy);
  }

  .contacts {
    position: absolute; left: 181px; top: 213px;
    font-size: 12px; font-weight: 400; line-height: 18px; color: var(--ink-soft);
  }
  .contacts__row { display: flex; align-items: center; gap: 4px; white-space: nowrap; }
  .contacts__icon { width: 10px; height: 10px; flex: none; }
  .contacts__gap { display: inline-block; width: 6px; }
  .contacts__email { font-size: 10.5px; }
</style>
</head>
<body>
<main class="canvas">

  <section class="card card--front" aria-label="Card front">
    <div class="lockup">
      <span class="lockup__dot"></span>
      <span class="lockup__name">Fenwicks</span>
      <span class="lockup__motto">Done Properly, Always</span>
    </div>

    <div class="address">
      <svg class="address__icon" viewBox="0 0 9 12" aria-hidden="true">
        <path d="M4.5 0C2 0 0 2 0 4.4 0 7.6 4.5 12 4.5 12S9 7.6 9 4.4C9 2 7 0 4.5 0zm0 6.2a1.8 1.8 0 1 1 0-3.6 1.8 1.8 0 0 1 0 3.6z" fill="var(--brand-navy)"/>
      </svg>
      <p class="address__text">Kestrel Vale Landfill &amp; Recycling Facility,<br>Wexcombe Rd, Marrowbank, WA 6197</p>
    </div>

    <div class="cert-badge" role="img" aria-label="Certification hologram">
      <span class="cert-badge__disc"></span>
    </div>
  </section>

  <section class="card card--back" aria-label="Card back">
    <div class="lockup lockup--ghost" aria-hidden="true">
      <span class="lockup__dot"></span>
      <span class="lockup__name">Fenwicks</span>
      <span class="lockup__motto">Done Properly, Always</span>
    </div>

    <div class="person">
      <p class="person__name">Bertolus Kemprano</p>
      <p class="person__role">Business Manager</p>
    </div>

    <span class="divider"></span>

    <div class="contacts">
      <p class="contacts__row">
        <svg class="contacts__icon" viewBox="0 0 12 12" aria-hidden="true">
          <path d="M2.4 0.6 4.2 2.6 3.3 4.1C4 5.6 6.4 8 7.9 8.7L9.4 7.8 11.4 9.6 10.3 11.3C6 11.6 0.4 6 0.7 1.7Z" fill="var(--brand-navy)"/>
        </svg>
        +61 8 5021 3748<span class="contacts__gap"></span>
        <svg class="contacts__icon" viewBox="0 0 12 12" aria-hidden="true">
          <rect x="2.5" y="0.5" width="7" height="11" rx="1.2" fill="none" stroke="var(--brand-navy)" stroke-width="1.3"/>
          <circle cx="6" cy="9.6" r="0.7" fill="var(--brand-navy)"/>
        </svg>
        +61 400 917 352
      </p>
      <p class="contacts__row">
        <svg class="contacts__icon" viewBox="0 0 12 12" aria-hidden="true">
          <rect x="0.6" y="2.2" width="10.8" height="7.6" rx="0.8" fill="none" stroke="var(--brand-navy)" stroke-width="1.1"/>
          <path d="M1 2.8 6 6.6 11 2.8" fill="none" stroke="var(--brand-navy)" stroke-width="1.1"/>
        </svg>
        <span class="contacts__email">bertie@fenwicksenvironmental-mail.example</span>
      </p>
    </div>
  </section>

</main>
</body>
</html>
```